'Orla Property Development' Business Card

Business Card Features:

High Quality (potentially textured) thick card - preference is white textured card

Logo (supplied)

We plan to use the vertical logo as the main logo. But i am happy for people to use either if they find it works better for the design of the card.

The building icon and also the insert to the 'E' is in a metallic finish, i think this should be finished in a metallic embossed or raised style.
Updates

Please note i have attached both a horizontal and Vertical Logo for your reference. We plan to use the vertical logo as the main logo. But i am happy for people to use either if they find it works better for the design of the card.

Please note i am considering having the cards made on stainless steel. This introduces the option of having cut outs in the card and etching or printing for the design. If you have a good concept for this please submit.

http://www.quorvantprint.co.uk/black-metal-cards# this is a site that makes the metal cards to offer some direction . . . . Please note i am basic the selection o the best design, if that means normal print cards on paper then this is what i will choose. But there are some great options with the metal. Thanks.

Industry/Entity Type

Building

Requirements
Must have
• Helvetica font to details side of card - logo as supplied to opposite side.

Card Details:

Darren Ashcombe
Managing Director

+61 438 615 207
+61 3 8276 4139

PO Box 73
Carrowby, Vic 3187

darren@orla.properties

www.orla.properties

```html
<!DOCTYPE html>
<html lang="en">
<head>
<meta charset="utf-8">
<title>Orla Property Development – Business Card</title>
<link href="https://fonts.googleapis.com/css2?family=Open+Sans:wght@400;600;700&display=swap" rel="stylesheet">
<style>
  :root {
    --backdrop: #e9e7e4;
    --card: #f6f5f2;
    --card-edge: #dedbd6;
    --ink: #4a4a4c;
    --ink-soft: #6b6b6e;
    --emboss: #e7e5e1;
    --emboss-shade: #d6d3ce;
    --metal-light: #ececec;
    --metal-mid: #b9b9bb;
    --metal-dark: #8e8e91;
  }
  * { box-sizing: border-box; margin: 0; padding: 0; }
  html, body {
    width: 896px; height: 1200px; overflow: hidden;
    background: var(--backdrop);
    font-family: "Open Sans", Arial, sans-serif;
    color: var(--ink);
  }
  .sheet {
    width: 896px; height: 1200px;
    display: flex; flex-direction: column; align-items: center; justify-content: space-around;
  }
  .card {
    position: relative;
    width: 600px; height: 366px;
    background: var(--card);
    box-shadow: 0 0 0 1px var(--card-edge), 0 6px 18px rgba(0,0,0,0.12);
    overflow: hidden;
  }

  /* Details side */
  .card-details .emboss-mark {
    position: absolute; left: 60px; top: 120px;
    width: 140px; height: 120px;
    display: flex; align-items: center; justify-content: center;
    font-size: 34px; font-weight: 700; letter-spacing: 2px;
    color: var(--emboss);
    text-shadow: 1px 1px 0 #ffffff, -1px -1px 0 var(--emboss-shade);
  }
  .name-band {
    position: absolute; left: 250px; right: 0; top: 116px;
    height: 68px;
    background: linear-gradient(100deg, var(--metal-mid) 0%, var(--metal-light) 45%, var(--metal-mid) 75%, var(--metal-dark) 100%);
    display: flex; align-items: baseline; padding: 24px 0 0 26px; gap: 10px;
  }
  .name-band .person-name {
    font-size: 17px; font-weight: 700; letter-spacing: 0.3px;
    text-transform: uppercase; color: var(--ink); white-space: nowrap;
  }
  .name-band .person-title {
    font-size: 12px; color: var(--ink-soft); white-space: nowrap;
  }
  .contact {
    position: absolute; right: 26px; bottom: 34px;
    font-size: 13px; color: var(--ink-soft);
    text-align: right; line-height: 26px;
  }
  .contact-line { display: flex; justify-content: flex-end; align-items: center; gap: 6px; white-space: nowrap; }
  .contact-line .sep { color: var(--metal-dark); }
  .contact-item { display: inline-flex; align-items: center; gap: 4px; }
  .icon { width: 13px; height: 13px; fill: none; stroke: var(--ink-soft); stroke-width: 1.4; }

  /* Logo side */
  .card-logo {
    display: flex; flex-direction: column; align-items: center; justify-content: center;
  }
  .brand-square {
    width: 86px; height: 86px;
    background: linear-gradient(135deg, var(--metal-light), var(--metal-mid) 60%, var(--metal-dark));
    margin-bottom: 22px;
  }
  .brand-name {
    font-size: 60px; font-weight: 700; letter-spacing: 6px; line-height: 1;
    color: var(--ink); text-transform: uppercase;
  }
  .brand-sub {
    font-size: 15px; font-weight: 700; letter-spacing: 2.5px; margin-top: 8px;
    color: var(--ink); text-transform: uppercase;
  }
</style>
</head>
<body>
<main class="sheet">

  <section class="card card-details" aria-label="Business card, details side">
    <div class="emboss-mark">ORLA</div>

    <div class="name-band">
      <span class="person-name">Darren Ashcombe</span>
      <span class="person-title">Managing Director</span>
    </div>

    <div class="contact">
      <div class="contact-line">
        <span class="contact-item">
          <svg class="icon" viewBox="0 0 14 14"><rect x="3.5" y="1" width="7" height="12" rx="1.2"/><line x1="6" y1="11" x2="8" y2="11"/></svg>
          +61 438 615 207
        </span>
        <span class="sep">|</span>
        <span class="contact-item">
          <svg class="icon" viewBox="0 0 14 14"><path d="M1.5 5 Q7 1 12.5 5 L11 6.5 L9.5 5 L4.5 5 L3 6.5 Z"/><rect x="3" y="7" width="8" height="5" rx="1"/></svg>
          +61 3 8276 4139
        </span>
        <span class="sep">|</span>
        <span class="contact-item">
          <svg class="icon" viewBox="0 0 14 14"><rect x="1" y="3" width="12" height="8"/><polyline points="1,3 7,8 13,3"/></svg>
          darren@orla.properties
        </span>
      </div>
      <div class="contact-line">
        <span class="contact-item">
          <svg class="icon" viewBox="0 0 14 14"><circle cx="7" cy="7" r="5.5"/><ellipse cx="7" cy="7" rx="2.4" ry="5.5"/><line x1="1.5" y1="7" x2="12.5" y2="7"/></svg>
          www.orla.properties
        </span>
        <span class="sep">|</span>
        <span class="contact-item">
          <svg class="icon" viewBox="0 0 14 14"><path d="M7 13 C3 8 3 6.5 3 5 A4 4 0 0 1 11 5 C11 6.5 11 8 7 13 Z"/><circle cx="7" cy="5" r="1.4"/></svg>
          PO Box 73, Carrowby, Vic 3187
        </span>
      </div>
    </div>
  </section>

  <section class="card card-logo" aria-label="Business card, logo side">
    <div class="brand-square"></div>
    <div class="brand-name">Orla</div>
    <div class="brand-sub">Property Development</div>
  </section>

</main>
</body>
</html>
```